TriVex Business Card Design - double sided -plumbing local plumbing company

We have a Plumbing company where the design was create through Sketch Hive. We would now like a business card designed as well. We want it to be in the colour version of the logo.

Details below for the card.

Phone Number: 0438 615 247
Email: info@trivexplumbing.example.au
Website: https://trivexplumbing.example.au
We really want a sophisticated design that stand out from the other- informative and timeless.

Target Market(s)

local Canberra market

Industry/Entity Type

Plumbing, gas fitting, hot water

Contact Information for Business Card

Phone number, email, logo and "Supplying all your heating, cooling and hot water needs"

Requirements
Must have
• bust be colourful, must also be though about it being printed on a magnet. must Vex with the logo - I dont want the logo and information chucked onto a white canvas I would prefer it to be smooth and look purposeful

```html
<!DOCTYPE html>
<html lang="en">
<head>
<meta charset="utf-8">
<title>TriVex Plumbing Business Card</title>
<link rel="stylesheet" href="https://fonts.googleapis.com/css2?family=Montserrat:wght@600;800&family=Work+Sans:wght@400;500&display=swap">
<style>
  :root {
    --stage: #2b2d2f;
    --navy: #0b1d3c;
    --navy-raised: #1a2d58;
    --sky: #1ea3e3;
    --amber: #f7a823;
    --white: #ffffff;
  }
  * { box-sizing: border-box; margin: 0; padding: 0; }
  html, body { width: 1200px; height: 939px; overflow: hidden; }
  body {
    background: var(--stage);
    position: relative;
    font-family: "Work Sans", sans-serif;
  }
  .card {
    position: absolute;
    width: 520px;
    height: 318px;
    background: var(--navy);
    border-radius: 2px;
    box-shadow: 0 14px 30px rgba(0,0,0,0.45);
    overflow: hidden;
  }
  .card--back { left: 60px; top: 90px; }
  .card--front { left: 620px; top: 530px; }

  .card__emboss {
    position: absolute;
    inset: 0;
    display: flex;
    align-items: center;
    justify-content: center;
    font-family: "Montserrat", sans-serif;
    font-weight: 800;
    font-size: 54px;
    letter-spacing: 1px;
    color: var(--navy-raised);
  }

  .brand {
    position: absolute;
    left: 34px;
    top: 118px;
    font-family: "Montserrat", sans-serif;
    font-weight: 800;
    font-size: 25px;
    line-height: 1.1;
    color: var(--sky);
  }
  .divider {
    position: absolute;
    left: 232px;
    top: 58px;
    width: 2px;
    height: 138px;
    background: var(--white);
  }
  .contact {
    position: absolute;
    left: 256px;
    top: 58px;
    color: var(--white);
  }
  .contact__name {
    font-family: "Montserrat", sans-serif;
    font-weight: 800;
    font-size: 22px;
    letter-spacing: 0.5px;
  }
  .contact__first { color: var(--sky); }
  .contact__last { color: var(--amber); }
  .contact__role {
    font-size: 11px;
    letter-spacing: 1.5px;
    margin: 2px 0 12px;
  }
  .contact__list { list-style: none; font-size: 11.5px; letter-spacing: 0.6px; }
  .contact__item {
    display: flex;
    align-items: center;
    gap: 8px;
    margin-bottom: 7px;
  }
  .contact__icon { width: 12px; height: 12px; flex: none; }
  .tagline {
    position: absolute;
    left: 0;
    right: 0;
    bottom: 34px;
    text-align: center;
    font-size: 14px;
    font-weight: 500;
    letter-spacing: 1px;
    color: var(--white);
  }
</style>
</head>
<body>
  <section class="card card--back" aria-label="Card back">
    <div class="card__emboss">TriVex Plumbing</div>
  </section>

  <section class="card card--front" aria-label="Card front">
    <div class="brand">TriVex<br>Plumbing</div>
    <div class="divider"></div>
    <div class="contact">
      <p class="contact__name"><span class="contact__first">REID</span> <span class="contact__last">MARLOW</span></p>
      <p class="contact__role">CEO</p>
      <ul class="contact__list">
        <li class="contact__item">
          <svg class="contact__icon" viewBox="0 0 24 24"><path fill="#1ea3e3" d="M6.6 10.8a15 15 0 0 0 6.6 6.6l2.2-2.2c.3-.3.7-.4 1-.2 1.1.4 2.3.6 3.6.6.6 0 1 .4 1 1V20c0 .6-.4 1-1 1A17 17 0 0 1 3 4c0-.6.4-1 1-1h3.5c.6 0 1 .4 1 1 0 1.3.2 2.5.6 3.6.1.3 0 .7-.2 1z"/></svg>
          <span>0438 615 247</span>
        </li>
        <li class="contact__item">
          <svg class="contact__icon" viewBox="0 0 24 24"><path fill="#1ea3e3" d="M2 5h20v14H2z"/><path fill="none" stroke="#0b1d3c" stroke-width="2" d="M2 5l10 8 10-8"/></svg>
          <span>info@trivexplumbing.example.au</span>
        </li>
        <li class="contact__item">
          <svg class="contact__icon" viewBox="0 0 24 24"><g fill="none" stroke="#1ea3e3" stroke-width="2"><circle cx="12" cy="12" r="9"/><path d="M3 12h18M12 3c3 3 3 15 0 18M12 3c-3 3-3 15 0 18"/></g></svg>
          <span>www.trivexplumbing.example.au</span>
        </li>
      </ul>
    </div>
    <p class="tagline">Supplying all your heating, cooling and hot water needs</p>
  </section>
</body>
</html>
```